Wedding invitation

We need a wedding invitation designed with a logo using our initials and name underneath.
We are getting married at THE BRENNA hotel in Gstaad and we would like have our logo similar to theirs but incorporating our initials n&g (any font/case) and our names below noreen and Gilberto. THE BRENNA logo can be seen on their website.
The invitation would be square with the logo on the front in stamped foil and the colour would be THE BRENNA brown (I have the exact colour)
THE BRENNA Brown: C45 M70 Y68 K77
THE BRENNA Rose Gold: VELMAR 218
Inside we would have the invitation wording and on the opposite side some contact info. There would be four inserts - accom, directions, brunch and RSVP. We will provide the wording.

```html
<!DOCTYPE html>
<html lang="en">
<head>
<meta charset="utf-8">
<title>Noreen &amp; Gilberto – Wedding Invitation</title>
<link rel="stylesheet" href="https://fonts.googleapis.com/css2?family=Open+Sans:wght@300;400;600&display=swap">
<style>
  :root {
    --brenna-brown: #3e231c;
    --rose-gold: #f08a66;
    --paper: #ffffff;
    --card-edge: #bdbdbd;
    --corner-grey: #c6c6c6;
    --ink: #4a4a4a;
    --ink-soft: #5c5c5c;
  }
  * { box-sizing: border-box; margin: 0; padding: 0; }
  html, body { width: 1200px; height: 900px; overflow: hidden; }
  body {
    position: relative;
    background: var(--paper);
    font-family: "Open Sans", sans-serif;
    color: var(--ink);
  }
  .card {
    position: absolute;
    top: 264px;
    width: 328px;
    height: 328px;
  }
  .card--front { left: 72px; background: var(--brenna-brown); }
  .card--invite { left: 436px; background: var(--paper); border: 1px solid var(--card-edge); }
  .card--accommodation { left: 799px; background: var(--paper); border: 1px solid var(--card-edge); }

  .corner { position: absolute; width: 50px; height: 50px; }
  .corner--top-right { top: 16px; right: 15px; border-top: 5px solid; border-right: 5px solid; }
  .corner--bottom-left { bottom: 15px; left: 16px; border-bottom: 5px solid; border-left: 5px solid; }
  .card--front .corner { border-color: var(--rose-gold); }
  .card--invite .corner, .card--accommodation .corner { border-color: var(--corner-grey); }

  .monogram {
    position: absolute;
    left: 0; right: 0;
    display: flex;
    justify-content: center;
    align-items: center;
    gap: 6px;
    font-weight: 300;
  }
  .monogram__ring { border-radius: 50%; border-style: solid; }
  .card--front .monogram { top: 118px; color: var(--rose-gold); font-size: 30px; }
  .card--front .monogram__ring { width: 14px; height: 14px; border-width: 1.5px; border-color: var(--rose-gold); }
  .card-inner-mark { top: 250px; color: var(--corner-grey); font-size: 20px; }
  .card-inner-mark .monogram__ring { width: 10px; height: 10px; border-width: 1px; border-color: var(--corner-grey); }

  .couple-names {
    position: absolute;
    top: 182px; left: 0; right: 0;
    text-align: center;
    color: var(--rose-gold);
    font-size: 13px;
    font-weight: 400;
    letter-spacing: 0.2px;
  }

  .card-title {
    position: absolute;
    top: 44px; left: 0; right: 0;
    text-align: center;
    font-size: 21px;
    font-weight: 300;
    letter-spacing: 0.6px;
    color: var(--ink);
  }

  .invite-wording {
    position: absolute;
    top: 122px; left: 0; right: 0;
    text-align: center;
    font-size: 7.6px;
    line-height: 10px;
    color: var(--ink-soft);
  }
  .invite-wording strong { font-weight: 600; color: var(--ink); }
  .invite-wording p + p { margin-top: 5px; }

  .accommodation-text {
    position: absolute;
    top: 87px; left: 18px; right: 18px;
    text-align: center;
    font-size: 7.4px;
    line-height: 10px;
    color: var(--ink-soft);
  }
  .accommodation-text p + p { margin-top: 10px; }
</style>
</head>
<body>

  <section class="card card--front" aria-label="Invitation front">
    <span class="corner corner--top-right"></span>
    <span class="corner corner--bottom-left"></span>
    <div class="monogram"><span class="monogram__ring"></span>N&amp;G</div>
    <p class="couple-names">NOREEN &amp; GILBERTO</p>
  </section>

  <section class="card card--invite" aria-label="Invitation wording">
    <span class="corner corner--top-right"></span>
    <span class="corner corner--bottom-left"></span>
    <h1 class="card-title">YOU ARE INVITED</h1>
    <div class="invite-wording">
      <p><strong>Clara &amp; Thomas</strong></p>
      <p>are invited to attend<br><strong>the wedding of Noreen &amp; Gilberto</strong></p>
      <p>at the Brenna Hotel, Gstaad<br>at time, date here 2014</p>
    </div>
    <div class="monogram card-inner-mark"><span class="monogram__ring"></span>N&amp;G</div>
  </section>

  <section class="card card--accommodation" aria-label="Accommodation insert">
    <span class="corner corner--top-right"></span>
    <span class="corner corner--bottom-left"></span>
    <h2 class="card-title">ACCOMMODATION</h2>
    <div class="accommodation-text">
      <p>Lorem ipsum dolor sit amet, consectetur adipiscing elit. Sed lacinia accumsan libero eget gravida. Vivamus dui ante, gravida sed nulla nec, varius nibh.</p>
      <p>Nulla lorem augue, vehicula sed felis eu, gravida vestibulum dui. Vivamus tempor, nisi euismod posuere molestie, tortor massa molestie lectus, vitae egestas dui felis sit amet magna. Integer laoreet risus in arcu semper, in vulputate augue rutrum. Cras vehicula quis ante id convallis.</p>
      <p>Nunc elementum vulputate libero id porttitor. Nullam mattis auctor mauris, vitae consequat odio vestibulum a. Ut quis velit sed lacus cursus laoreet et at tortor. Ut eu massa est. Aliquam lacinia blandit orci imperdiet consectetur. Cras dapibus mollis nisl vitae accumsan.</p>
      <p>Maecenas vulputate leo ut ligula tincidunt interdum.</p>
    </div>
    <div class="monogram card-inner-mark"><span class="monogram__ring"></span>N&amp;G</div>
  </section>

</body>
</html>
```